National Sales Meeting Agenda (Rodeo Theme)

I need a talented designer to create a visually stunning, single-page agenda for our upcoming National Sales Meeting. The design should reflect our brand’s colors and style, with a subtle rodeo theme, while maintaining a professional and polished look.
Key Requirements:
Theme: Subtle rodeo vibe with clean, Western-inspired elements that align with our brand identity.
Branding: Prominently feature the KORU BLEND TX logo, with a smaller MARLOT logo included.
Layout: Single page, clean, sharp, and easy to read.
Content: Include the meeting date (June 6-7) and location (Pinecrest Lodge Resort Scottsdale) at the top.
Formats: High-quality, print-ready PDF + editable file (Canva or InDesign) for updates.
Timeline: First draft within 1-2 days, final version by May 23rd.
Deliverables:
Print-ready PDF
Editable file for future updates
Design that captures our brand tone and subtle rodeo theme
Please visit korublendtx.example for brand inspiration. Let me know if you have any questions or need additional assets. Looking forward to seeing your creative ideas!
Target Market(s)
Medical Device Sales Reps

```html
<!DOCTYPE html>
<html lang="en">
<head>
<meta charset="utf-8">
<title>National Sales Meeting Agenda</title>
<link href="https://fonts.googleapis.com/css2?family=Saira+Condensed:wght@500;600;700&family=Roboto+Condensed:wght@400;500&display=swap" rel="stylesheet">
<style>
  :root {
    --navy: #0f1f4b;
    --blue: #2f3f8a;
    --ink: #2a2a33;
    --muted: #6a6a72;
    --rule: #4a4a55;
    --dots: #b5b5bc;
    --paper: #f7f7f8;
    --edge: #dcdce0;
  }
  * { margin: 0; padding: 0; box-sizing: border-box; }
  html, body { width: 849px; height: 1200px; overflow: hidden; }
  body {
    font-family: "Roboto Condensed", sans-serif;
    color: var(--ink);
    background: var(--paper);
  }
  .agenda {
    position: relative;
    width: 849px;
    height: 1200px;
    background: radial-gradient(ellipse at 50% 45%, #fbfbfc 55%, var(--edge) 100%);
    overflow: hidden;
  }
  .title-ribbon { position: absolute; left: 192px; top: 34px; width: 462px; height: 72px; }
  .title {
    position: absolute; left: 250px; top: 38px; width: 342px; height: 52px;
    font-family: "Saira Condensed", sans-serif; font-weight: 500;
    font-size: 39px; line-height: 52px; color: #fff; text-align: center;
  }
  .subtitle {
    position: absolute; left: 0; width: 849px; text-align: center;
    font-family: "Saira Condensed", sans-serif;
  }
  .subtitle.kicker { top: 98px; font-size: 20px; color: var(--navy); letter-spacing: 0.5px; }
  .subtitle.date { top: 124px; font-size: 21px; color: var(--muted); }
  .subtitle.day-two { top: 684px; }

  .col-head {
    position: absolute; font-family: "Saira Condensed", sans-serif;
    font-weight: 600; font-size: 19px; color: var(--navy);
  }
  .rule { position: absolute; left: 68px; width: 713px; height: 1px; background: var(--rule); }

  .row { position: absolute; left: 0; width: 849px; height: 22px; font-size: 15.5px; line-height: 22px; }
  .row .time { position: absolute; right: 706px; }
  .row .topic { position: absolute; left: 167px; white-space: nowrap; }
  .row .leader { position: absolute; left: 385px; width: 258px; top: 11px; border-top: 1px dotted var(--dots); }
  .row.wide .leader { left: 485px; width: 158px; }
  .row.medium .leader { left: 372px; width: 271px; }
  .row .star { position: absolute; left: 59px; top: 2px; width: 18px; height: 18px; fill: var(--navy); }
  .row.marker .topic {
    font-family: "Saira Condensed", sans-serif; font-weight: 600; font-size: 16.5px; color: var(--navy);
  }
  .row.marker.light .topic { color: var(--blue); }

  .presenter { position: absolute; font-size: 15.5px; line-height: 22px; white-space: nowrap; }
  .presenter.right { right: 69px; text-align: right; }

  .split { position: absolute; top: 468px; font-size: 15px; line-height: 17px; }
  .split h3 { font-weight: 400; font-size: 15.5px; margin-bottom: 2px; }
  .split ul { list-style: none; font-size: 13.5px; }
  .split li::before { content: "• "; }
  .split.managers { left: 167px; }
  .split.associates { left: 368px; }
  .split.associates li { margin-bottom: 4px; }

  .brand {
    position: absolute; left: 75px; top: 1070px;
    font-family: "Saira Condensed", sans-serif; font-weight: 600;
    font-size: 50px; line-height: 1; color: var(--navy); letter-spacing: 1px;
  }
  .scene {
    position: absolute; left: 395px; top: 1030px; width: 400px; height: 137px;
    border-radius: 0 0 14px 14px;
    background: linear-gradient(180deg, #fbfbfc 0%, #e9a3dd 45%, #c46bbb 68%, #1b1a45 82%, #0f1f4b 100%);
  }
  .partner {
    position: absolute; left: 703px; top: 1130px;
    font-family: "Saira Condensed", sans-serif; font-weight: 500;
    font-size: 20px; color: #fff; letter-spacing: 0.5px;
  }
</style>
</head>
<body>
<main class="agenda">
  <svg class="title-ribbon" viewBox="0 0 462 72" aria-hidden="true">
    <polygon fill="#0f1f4b" points="0,16 56,16 56,72 2,72 18,44"/>
    <polygon fill="#0f1f4b" points="462,14 404,14 404,72 460,72 434,40"/>
    <rect x="58" y="4" width="344" height="56" fill="#0f1f4b"/>
  </svg>
  <h1 class="title">National Sales Meeting</h1>
  <p class="subtitle kicker">AGENDA</p>
  <p class="subtitle date">Friday, June 6, 2025</p>

  <span class="col-head" style="left:92px;top:173px">TIME</span>
  <span class="col-head" style="left:169px;top:173px">TOPIC DESCRIPTION</span>
  <span class="col-head" style="left:667px;top:173px">PRESENTER</span>
  <div class="rule" style="top:197px"></div>

  <div class="row marker" style="top:213px"><svg class="star" viewBox="0 0 24 24"><path d="M12 1l3.1 7.6 8.2.6-6.3 5.3 2 8-7-4.4-7 4.4 2-8L.7 9.2l8.2-.6z"/></svg><span class="time">7:30 am</span><span class="topic">BREAKFAST</span></div>
  <div class="row" style="top:246px"><span class="time">8:30 am</span><span class="topic">Welcome &amp; Meeting Overview</span><span class="leader"></span></div>
  <div class="row" style="top:278px"><span class="time">9:00 am</span><span class="topic">MRI Review Exercise</span><span class="leader"></span></div>
  <div class="row marker" style="top:310px"><svg class="star" viewBox="0 0 24 24"><path d="M12 1l3.1 7.6 8.2.6-6.3 5.3 2 8-7-4.4-7 4.4 2-8L.7 9.2l8.2-.6z"/></svg><span class="time">9:45 am</span><span class="topic">BREAK</span></div>
  <div class="row" style="top:342px"><span class="time">10:00 am</span><span class="topic">Objection Handling</span><span class="leader"></span></div>
  <div class="row" style="top:374px"><span class="time">11:00 am</span><span class="topic">CEV Expectations</span><span class="leader"></span></div>
  <div class="row marker" style="top:406px"><svg class="star" viewBox="0 0 24 24"><path d="M12 1l3.1 7.6 8.2.6-6.3 5.3 2 8-7-4.4-7 4.4 2-8L.7 9.2l8.2-.6z"/></svg><span class="time">11:30 am</span><span class="topic">LUNCH</span></div>
  <div class="row" style="top:438px"><span class="time">12:00 pm</span><span class="topic">Afternoon Split Session</span><span class="leader"></span></div>

  <div class="split managers">
    <h3>Area Sales Managers</h3>
    <ul><li>Leadership<br>&nbsp;&nbsp;Training</li><li>Field Operations</li></ul>
  </div>
  <div class="split associates">
    <h3>Associate Sales Representatives</h3>
    <ul><li>APP Training</li><li>Coding &amp; Reimbursement</li></ul>
  </div>

  <div class="row" style="top:566px"><span class="time">1:00 pm</span><span class="topic">Role Plays</span><span class="leader"></span></div>
  <div class="row" style="top:599px"><span class="time">1:30 pm</span><span class="topic">Day One Closing</span><span class="leader"></span></div>
  <div class="row marker" style="top:640px"><svg class="star" viewBox="0 0 24 24"><path d="M12 1l3.1 7.6 8.2.6-6.3 5.3 2 8-7-4.4-7 4.4 2-8L.7 9.2l8.2-.6z"/></svg><span class="time">2:00 pm</span><span class="topic">ADJOURN - RIVER RODEO</span></div>

  <span class="presenter right" style="top:247px">Dale Porter Owen</span>
  <span class="presenter right" style="top:275px">Hale</span>
  <span class="presenter right" style="top:344px">Grant Fell Dale</span>
  <span class="presenter right" style="top:372px">Porter</span>
  <span class="presenter right" style="top:406px">ALL</span>
  <span class="presenter right" style="top:565px;right:77px">Blake Sorensen</span>
  <span class="presenter right" style="top:598px;right:61px">&amp; Jordan Whitaker</span>
  <span class="presenter right" style="top:623px;right:61px">Ray Castillo</span>

  <p class="subtitle date day-two">Saturday, June 7, 2025</p>

  <span class="col-head" style="left:92px;top:737px">TIME</span>
  <span class="col-head" style="left:167px;top:737px">TOPIC DESCRIPTION</span>
  <span class="col-head" style="left:693px;top:737px">PRESENTER</span>
  <div class="rule" style="top:763px"></div>

  <div class="row marker light" style="top:777px"><svg class="star" viewBox="0 0 24 24"><path d="M12 1l3.1 7.6 8.2.6-6.3 5.3 2 8-7-4.4-7 4.4 2-8L.7 9.2l8.2-.6z"/></svg><span class="time">7:30 am</span><span class="topic">BREAKFAST</span></div>
  <div class="row wide" style="top:809px"><span class="time">8:30 am</span><span class="topic">RENEW &amp; CLIMB Clinical Study Discussion</span><span class="leader"></span></div>
  <div class="row wide" style="top:844px"><span class="time">9:00 am</span><span class="topic">NP Pilot 6 month, 12month, and 24 month Data</span><span class="leader"></span></div>
  <div class="row marker light" style="top:876px"><svg class="star" viewBox="0 0 24 24"><path d="M12 1l3.1 7.6 8.2.6-6.3 5.3 2 8-7-4.4-7 4.4 2-8L.7 9.2l8.2-.6z"/></svg><span class="time">10:00 am</span><span class="topic">BREAK</span></div>
  <div class="row medium" style="top:913px"><span class="time">10:15 am</span><span class="topic">Veterans Administration</span><span class="leader"></span></div>
  <div class="row medium" style="top:948px"><span class="time">11:00 am</span><span class="topic">Marketing Update</span><span class="leader"></span></div>
  <div class="row medium" style="top:980px"><span class="time">11:30 am</span><span class="topic">2025 NSM Meeting Close</span><span class="leader"></span></div>
  <div class="row marker light" style="top:1012px"><svg class="star" viewBox="0 0 24 24"><path d="M12 1l3.1 7.6 8.2.6-6.3 5.3 2 8-7-4.4-7 4.4 2-8L.7 9.2l8.2-.6z"/></svg><span class="time">11:45 am</span><span class="topic">ADJOURN</span></div>

  <span class="presenter" style="left:654px;top:807px">Carly Benson Tess</span>
  <span class="presenter" style="left:654px;top:828px">Moreau</span>
  <span class="presenter" style="left:654px;top:849px">Lauren Seidel</span>
  <span class="presenter right" style="top:914px;right:63px">&amp; Ross Maddox</span>
  <span class="presenter right" style="top:946px;right:63px">Paige Walton</span>
  <span class="presenter right" style="top:979px;right:63px">Dale Porter</span>

  <div class="brand">KORU BLEND TX</div>
  <div class="scene" role="img" aria-label="Desert landscape with a rider on horseback swinging a lasso beside a tall cactus, pink hills at dusk"></div>
  <span class="partner">MARLOT</span>
</main>
</body>
</html>
```